Online-Marketing Material
wir sind sehr zufrieden mit allem. danke
Zielgruppe
Wir vertreiben auf unserer Plattform morvelhaus17.de diverse Produkte rund um das Thema Kaffee. Unsere Zielgruppe sind Kaffeeliebhaber von jung bis alt.
Aufgabenstellung
Für unsere neue Domain brulino.at benötigen wir diverse Grafiken / Banner für die verschiedenen Bereiche unseres Shops. Momentan gibt es eine Staging Site um sich einen Überblick zu verschaffen.
Auftrag hier ist ein Startseitenbanner in der Größe 3200x1240 unter Berücksichtigung der aktuellen Farben in unserem Shop, der Thematik Kaffee und mehr und dem dazugehörigen neuen bereits entworfenem Logo.
Info Testseite: http://www.brulino.at/_staging/ Login mit admin und velo#482
Gerne kann eigenes Bildmaterial geliefert werden

```html
<!DOCTYPE html>
<html lang="de">
<head>
<meta charset="utf-8">
<title>brulino.at – Kaffeespezialitäten</title>
<link href="https://fonts.googleapis.com/css2?family=Montserrat:wght@400;700&display=swap" rel="stylesheet">
<style>
  :root {
    --brand-red: #be0020;
    --brand-brown: #3a2419;
    --sand: #e6d2bb;
    --sand-ring: #d6bea2;
    --white: #ffffff;
    --bean-gold: #d9935a;
  }
  html, body {
    margin: 0;
    padding: 0;
    overflow: hidden;
  }
  .banner {
    position: relative;
    width: 1200px;
    height: 465px;
    overflow: hidden;
    background: var(--sand);
    font-family: "Montserrat", sans-serif;
  }
  .backdrop {
    position: absolute;
    left: 0;
    top: 0;
  }
  .headline-band {
    position: absolute;
    left: 0;
    top: 0;
    width: 1013px;
    height: 84px;
    background: var(--brand-red);
    display: flex;
    align-items: center;
  }
  .headline {
    margin: 0 0 0 28px;
    color: var(--white);
    font-weight: 400;
    font-size: 46px;
    line-height: 1;
    white-space: nowrap;
  }
  .brand-box {
    position: absolute;
    left: 1013px;
    top: 0;
    width: 158px;
    height: 84px;
    background: var(--brand-brown);
    display: flex;
    align-items: flex-end;
    justify-content: center;
    padding-bottom: 13px;
    box-sizing: border-box;
  }
  .brand-name {
    color: var(--white);
    font-weight: 700;
    font-size: 16px;
  }
  .cta {
    position: absolute;
    left: 947px;
    top: 390px;
    width: 224px;
    height: 54px;
    box-sizing: border-box;
    border: 3px solid var(--white);
    display: flex;
    text-decoration: none;
  }
  .cta-icon {
    width: 63px;
    background: var(--brand-brown);
    display: flex;
    align-items: center;
    justify-content: center;
  }
  .cta-label {
    flex: 1;
    background: var(--brand-red);
    color: var(--white);
    font-size: 25px;
    display: flex;
    align-items: center;
    justify-content: center;
  }
</style>
</head>
<body>
  <div class="banner">
    <svg class="backdrop" width="1200" height="465" viewBox="0 0 1200 465">
      <defs>
        <filter id="soft-edge" x="-5%" y="-5%" width="110%" height="110%">
          <feGaussianBlur stdDeviation="4"/>
        </filter>
        <radialGradient id="cups-tone" cx="40%" cy="45%" r="70%">
          <stop offset="0" stop-color="#5a3b27"/>
          <stop offset="0.45" stop-color="#a67c5a"/>
          <stop offset="1" stop-color="#eee3d5"/>
        </radialGradient>
        <linearGradient id="cherry-tone" x1="0" y1="0" x2="1" y2="1">
          <stop offset="0" stop-color="#c0182f"/>
          <stop offset="0.45" stop-color="#a3122a"/>
          <stop offset="0.75" stop-color="#3f6a2c"/>
          <stop offset="1" stop-color="#2e5524"/>
        </linearGradient>
      </defs>

      <g class="rings" fill="none" stroke="var(--sand-ring)" stroke-width="14" aria-hidden="true">
        <circle cx="725" cy="228" r="166"/>
        <circle cx="725" cy="228" r="134"/>
        <circle cx="725" cy="228" r="102"/>
      </g>

      <path class="cups-photo" role="img" aria-label="Von oben fotografierte Kaffeetassen mit Espresso, Cappuccino und Latte Art"
            fill="url(#cups-tone)" filter="url(#soft-edge)"
            d="M-10,84 H575 C600,170 598,260 565,320 C520,390 410,440 350,475 H-10 Z"/>

      <path class="cherries-photo" role="img" aria-label="Zweig eines Kaffeestrauchs mit roten Kaffeekirschen und grünen Blättern"
            fill="url(#cherry-tone)" filter="url(#soft-edge)"
            d="M335,475 C335,390 390,300 470,272 C525,252 570,175 612,125 C660,98 760,100 830,88 L1160,84 L1160,-10 H1210 V475 H705 C695,405 680,352 640,335 C600,322 570,400 540,475 Z"/>
    </svg>

    <header class="headline-band">
      <h1 class="headline">Kaffeespezialitäten für jeden Geschmack!</h1>
    </header>

    <div class="brand-box">
      <span class="brand-name">brulino.at</span>
    </div>

    <a class="cta" href="#">
      <span class="cta-icon">
        <svg width="30" height="40" viewBox="0 0 30 40" aria-hidden="true">
          <ellipse cx="15" cy="20" rx="12" ry="17" fill="none" stroke="var(--bean-gold)" stroke-width="2.5"/>
          <path d="M15 4 C9 14, 21 26, 15 36" fill="none" stroke="var(--bean-gold)" stroke-width="2.5"/>
        </svg>
      </span>
      <span class="cta-label">Mehr Infos</span>
    </a>
  </div>
</body>
</html>
```